redesing professional certificate

Redesign our certificate to more a professional look and to make it look like a-wanna have - Best in adobe photoshop, because this template will be our basic, and we have in our education different levels, basic, upper, lower, complex, master level. I usually add a small picture to show what level they are. Or when you have a better suggestion I a gladly to hear.
We teach to physiotherapist so it has to look professional.

Target Market(s)

physiotherapist

Industry/Entity Type

Health Care

Requirements
Must have
• our logo

```html
<!DOCTYPE html>
<html lang="en">
<head>
<meta charset="utf-8">
<title>Meridia Fascia Method – Certificate</title>
<link href="https://fonts.googleapis.com/css2?family=Cinzel:wght@400&family=Playfair+Display:wght@700&family=Poppins:wght@400;500;600;700&display=swap" rel="stylesheet">
<style>
  :root {
    --navy: #1b2a4a;
    --navy-text: #22395f;
    --gold: #d4a52a;
    --gold-line: #c9a24a;
    --paper: #f7f7f8;
    --ink: #2b2b33;
    --backdrop: #e4e4e6;
    --green-dark: #2f6b1c;
    --green-light: #8fd34a;
  }
  * { box-sizing: border-box; margin: 0; padding: 0; }
  html, body { width: 1200px; height: 862px; overflow: hidden; }
  body { background: var(--backdrop); font-family: "Poppins", sans-serif; color: var(--ink); }

  .certificate {
    position: absolute; left: 318px; top: 31px;
    width: 564px; height: 800px;
    background: var(--navy);
  }
  .certificate__sheet {
    position: absolute; left: 15px; top: 17px; right: 15px; bottom: 17px;
    background: var(--paper);
    border: 2px solid var(--gold-line);
    border-radius: 19px;
  }
  .sheet-item { position: absolute; left: 0; right: 0; text-align: center; }

  .brand-seal {
    position: absolute; left: 208px; top: 13px;
    width: 148px; height: 148px; border-radius: 50%;
    background: var(--navy);
    border: 2px solid #d9d9de;
    display: flex; align-items: center; justify-content: center; text-align: center;
  }
  .brand-seal__name {
    font-family: "Poppins", sans-serif; font-weight: 700;
    color: #ffffff; font-size: 17px; line-height: 1.2; letter-spacing: 0.5px;
  }

  .title-rule { top: 178px; height: 6px; }
  .title-rule svg { display: block; margin: 0 auto; }

  .certificate__title {
    top: 188px;
    font-family: "Cinzel", serif; font-weight: 400;
    font-size: 39px; letter-spacing: 3px; color: var(--navy-text);
  }
  .title-flourish {
    position: absolute; left: 213px; top: 246px;
    width: 137px; height: 26px; border-radius: 50%;
    background: radial-gradient(ellipse at center, rgba(34,57,95,0.35), rgba(34,57,95,0));
  }

  .recipient-name {
    top: 322px;
    font-family: "Playfair Display", serif; font-weight: 700;
    font-size: 30px; letter-spacing: 1px; color: var(--navy-text);
  }
  .course-details { top: 376px; font-size: 14px; line-height: 20px; color: var(--ink); }
  .course-details strong { font-weight: 600; }

  .signatories { top: 500px; display: flex; justify-content: center; }
  .signatory { width: 190px; text-align: center; }
  .signatory__name { font-weight: 600; font-size: 17px; color: var(--navy-text); line-height: 24px; }
  .signatory__role { font-size: 13px; color: var(--navy-text); line-height: 22px; margin-top: 2px; }
  .signatories__divider { width: 1px; height: 38px; background: #9aa0ab; margin: 4px 3px 0; }

  .registration { top: 570px; font-weight: 700; font-size: 12.5px; color: var(--gold); letter-spacing: 0.2px; }
  .maintenance-note { top: 593px; font-size: 11.5px; line-height: 14.5px; color: var(--ink); padding: 0 30px; }

  .issuer { position: absolute; left: 37px; top: 654px; font-size: 11.5px; line-height: 18px; color: var(--ink); }
  .issuer__tagline { margin-top: 14px; font-size: 14px; }
  .issuer__tagline strong { font-weight: 600; }

  .level-badge {
    position: absolute; left: 372px; top: 634px;
    width: 122px; height: 122px; border-radius: 50%;
    border: 3px solid var(--gold-line);
    background: radial-gradient(circle at 55% 45%, var(--green-light), var(--green-dark) 85%);
  }
</style>
</head>
<body>
  <main class="certificate">
    <section class="certificate__sheet">
      <div class="brand-seal">
        <span class="brand-seal__name">MERIDIA<br>FASCIA<br>METHOD</span>
      </div>

      <div class="sheet-item title-rule">
        <svg width="330" height="6" viewBox="0 0 330 6" aria-hidden="true">
          <line x1="0" y1="3" x2="120" y2="3" stroke="#22395f" stroke-width="1.2"/>
          <line x1="210" y1="3" x2="330" y2="3" stroke="#22395f" stroke-width="1.2"/>
          <circle cx="3" cy="3" r="2.5" fill="#22395f"/>
          <circle cx="327" cy="3" r="2.5" fill="#22395f"/>
        </svg>
      </div>

      <h1 class="sheet-item certificate__title">CERTIFICATE</h1>
      <div class="title-flourish" role="img" aria-label="Decorative calligraphic flourish under the title"></div>

      <h2 class="sheet-item recipient-name">MARTA LINDQVIST</h2>
      <p class="sheet-item course-details">
        has completed the <strong>fascia therapy level I course</strong><br>
        - 3 days, 75-77 february 2020 -<br>
        Kópavogur, Iceland 77 february 2020.
      </p>

      <div class="sheet-item signatories">
        <div class="signatory">
          <p class="signatory__name">Mr. JT Hollander</p>
          <p class="signatory__role">Co-Director</p>
        </div>
        <div class="signatories__divider"></div>
        <div class="signatory">
          <p class="signatory__name">Mr. RB Okafor</p>
          <p class="signatory__role">Co-Director</p>
        </div>
      </div>

      <p class="sheet-item registration">REGISTRATION NUMBER: 1 ICE 20</p>
      <p class="sheet-item maintenance-note">
        The Meridia Fascia Method ongoing certification is contingent upon meeting<br>
        the requirements of the maintenance of the certification of Fasciatherapy
      </p>

      <address class="issuer" style="font-style: normal;">
        Tensora BV<br>
        Keizerslaan 14<br>
        3511AB Utrecht<br>
        The Netherlands
        <p class="issuer__tagline">Specialists in <strong>Fasciatherapy innovation</strong></p>
      </address>

      <div class="level-badge" role="img" aria-label="Course level image: green tensegrity model in a gold-rimmed circle"></div>
    </section>
  </main>
</body>
</html>
```